Pounce! A stand up comedy show- poster and other graphics required

We require a design for a new late night comedy show called 'Pounce!' which will appear at festivals and feature a variety of stand up acts as well as inviting the audience to heckle the comedians on stage. The final design should be bold and stand out loudly, to fit the late night raucous nature of the show.
We need a poster image as well as smaller images for program guides and websites. This is going to be the kind of show people talk about so needs a poster to match!!

Target Market(s)

Comedy fans, 20-40 year olds, late night adult audience

Requirements
Nice to have
• We don't really have any clear design in mind so happy to leave it to interpretation but possible ideas would be: a silhouette of a head shouting / a mic is always an iconic image / the simple outline of an audience with obscenities (@*!& etc) coming out of them / perhaps a mic having fallen over because of a stand-up running off stage!
• But again these are vague ideas. Please message for more info about the show if it helps
Should not have
• Not too busy

```html
<!DOCTYPE html>
<html lang="en">
<head>
<meta charset="utf-8">
<title>Pounce! – Late Night Stand-Up</title>
<link rel="stylesheet" href="https://fonts.googleapis.com/css2?family=Spicy+Rice&display=swap">
<style>
  :root {
    --night: #03041a;
    --curtain: #080c52;
    --curtain-fold: rgba(40, 55, 210, 0.22);
    --curtain-shade: rgba(0, 0, 20, 0.35);
    --spot: rgba(45, 60, 255, 0.9);
    --footlight: rgba(70, 90, 240, 0.45);
    --floor: #0c1496;
    --floor-deep: #080e78;
    --performer: rgba(2, 3, 14, 0.92);
    --title: #f6ad2e;
  }
  * { margin: 0; padding: 0; box-sizing: border-box; }
  html, body { width: 1200px; height: 932px; overflow: hidden; background: var(--night); }

  .poster {
    position: relative;
    width: 1200px;
    height: 932px;
    overflow: hidden;
    background: linear-gradient(to bottom, var(--night) 0%, var(--curtain) 45%, #0c137a 62%, #121a8c 70%);
  }

  .curtain {
    position: absolute;
    left: 0; right: 0; top: 0;
    height: 665px;
    background:
      repeating-linear-gradient(to right,
        var(--curtain-shade) 0px, transparent 9px, var(--curtain-fold) 17px, transparent 26px,
        var(--curtain-shade) 31px, transparent 40px, var(--curtain-fold) 47px, transparent 55px);
    -webkit-mask-image: linear-gradient(to bottom, rgba(0,0,0,0.35) 0%, #000 55%, #000 100%);
            mask-image: linear-gradient(to bottom, rgba(0,0,0,0.35) 0%, #000 55%, #000 100%);
  }

  .footlights {
    position: absolute;
    left: 0; right: 0;
    top: 560px; height: 105px;
    background: linear-gradient(to bottom, rgba(70,90,240,0) 0%, var(--footlight) 55%, rgba(70,90,240,0.15) 100%);
  }

  .floor {
    position: absolute;
    left: 0; right: 0;
    top: 665px; bottom: 0;
    background:
      repeating-linear-gradient(to right,
        rgba(0,0,30,0.18) 0px, transparent 14px, rgba(50,70,230,0.18) 28px, transparent 42px),
      linear-gradient(to bottom, var(--floor) 0%, var(--floor-deep) 100%);
  }

  .spotlight {
    position: absolute;
    left: 420px; top: -40px;
    width: 400px; height: 620px;
    border-radius: 50% 50% 30% 30% / 40% 40% 20% 20%;
    background: radial-gradient(ellipse at 50% 25%, var(--spot) 0%, rgba(35,45,220,0.55) 35%, rgba(20,30,160,0) 72%);
  }

  .performer {
    position: absolute;
    left: 420px; top: 92px;
    width: 380px; height: 700px;
    background: radial-gradient(ellipse 48% 52% at 50% 50%, var(--performer) 0%, rgba(2,3,14,0.85) 55%, rgba(2,3,14,0) 100%);
  }

  .performer-shadow {
    position: absolute;
    left: 470px; top: 770px;
    width: 280px; height: 70px;
    border-radius: 50%;
    background: radial-gradient(ellipse at 50% 50%, rgba(5,8,50,0.6) 0%, rgba(5,8,50,0) 70%);
  }

  .show-title {
    position: absolute;
    left: 0; right: 0;
    top: 352px;
    text-align: center;
    font-family: "Spicy Rice", "Georgia", serif;
    font-weight: 400;
    font-size: 205px;
    line-height: 1;
    letter-spacing: 4px;
    color: var(--title);
  }
</style>
</head>
<body>
  <main class="poster">
    <div class="curtain"></div>
    <div class="footlights"></div>
    <div class="floor"></div>
    <div class="spotlight"></div>
    <div class="performer-shadow"></div>
    <div class="performer" role="img" aria-label="Silhouette of a comedian in a suit standing in the spotlight, shrugging with both hands raised"></div>
    <h1 class="show-title">Pounce!</h1>
  </main>
</body>
</html>
```